RM Skyline Imaging Web Site design

I am looking for a responsive single page website deign for rmskylineimages.com. This is a drone based aerial photography and cinematography business. It should have an about us section, a services section that contains photograph service, Video footage, and Aerial mapping all under the services section, a pricing section, and then a contact page for customers to contact us.

Coding

Coded - Design and coding required

Number of Pages Required

1 page

Font styles to use
Sans Serif

Colors

Designer to choose colors to be used in the design.

Requirements
Must have
• Responsive design. About us section, services section, pricing section under the services links, and contact us section, that links to a submission page where they can send Name, address, email, and comments on what they are interested in.
• See hoverlens7.com - looking for similar design.
Should not have
• clutter, or too busy design

```html
<!DOCTYPE html>
<html lang="en">
<head>
<meta charset="utf-8">
<title>RM Skyline Imaging</title>
<link rel="stylesheet" href="https://fonts.googleapis.com/css2?family=Orbitron:wght@500;700&family=Open+Sans:wght@400;600&display=swap">
<style>
:root{
  --ink:#1a1a1a;
  --orange:#f39322;
  --orange-dark:#c9731a;
  --navy:#2b2a7a;
  --blue:#2a2f8f;
  --grey:#8a8a8a;
  --footer:#262626;
  --footer-text:#b4b4b4;
  --white:#ffffff;
}
*{margin:0;padding:0;box-sizing:border-box}
html,body{width:701px;height:1200px;overflow:hidden;background:#fff}
body{position:relative;font-family:"Open Sans",Arial,sans-serif;color:var(--ink)}
.abs{position:absolute}
.display{font-family:"Orbitron","Arial Narrow",sans-serif}

.nav{left:0;top:0;width:701px;height:33px;background:#000}
.nav a{position:absolute;top:12px;font-size:7px;color:#d8d8d8;text-decoration:none}
.nav a.active{color:var(--orange)}
.nav .underline{position:absolute;left:93px;top:31px;width:38px;height:2px;background:var(--orange)}

.hero{left:0;top:33px;width:701px;height:308px;background:linear-gradient(180deg,#5d5048 0%,#6c5a4a 25%,#3b3632 55%,#24211f 100%)}
.hero-logo{left:285px;top:99px;width:131px;height:54px;background:#fff;display:flex;align-items:center;justify-content:center;font-size:8px;font-weight:600;color:var(--ink);letter-spacing:.5px}
.hero-title{left:0;top:180px;width:701px;text-align:center;color:#fff;font-size:23px;font-weight:700}
.hero-sub{left:0;top:208px;width:701px;text-align:center;color:#fff;font-size:17px;font-weight:500}

.about{left:0;top:341px;width:701px;height:64px;background:var(--orange)}
.about-label{left:93px;top:358px;color:#fff;font-size:9px;font-weight:700}
.about-title{left:93px;top:369px;color:#fff;font-size:14px;font-weight:700}
.about-text{left:294px;top:352px;width:320px;color:#fff;font-size:6.4px;line-height:10.2px}

.services{left:0;top:405px;width:701px;height:181px;background:#f9f9f9}
.section-head{width:701px;left:0;text-align:center;font-weight:700}
.services-rule{left:254px;top:465px;width:184px;height:1px;background:#dcdcdc}
.service-name{font-size:9px;font-weight:600;color:var(--blue)}
.service-desc{font-size:6.6px;color:var(--grey);line-height:9.5px;width:140px}

.pricing{left:0;top:586px;width:701px;height:193px;background:linear-gradient(180deg,#3a3a3c,#2a2b2e 60%,#222325)}
.pricing-title{left:93px;top:611px;color:#fff;font-size:13px;font-weight:700}
.plan{width:135px;height:79px;top:641px;border:1px solid #e8e8e8;color:#fff;text-align:center}
.plan-price{font-size:23px;font-weight:700;margin-top:11px}
.plan-note{font-size:6.6px;font-weight:500;letter-spacing:.4px;line-height:10px;margin-top:2px}
.plan-desc{top:729px;width:140px;color:#e6e6e6;font-size:6.6px;line-height:10px}

.contact{left:0;top:779px;width:701px;height:274px;background:#fbfbfb}
.field{background:#fff;border:1px solid #e4e4e4;font-size:6.6px;color:#666;padding:11px 12px}
.send{left:131px;top:988px;width:438px;height:25px;background:var(--navy);color:#fff;font-size:7px;text-align:center;line-height:25px;border-radius:2px}

.footer{left:0;top:1053px;width:701px;height:147px;background:var(--footer)}
.footer-head{color:#fff;font-size:8.5px;font-weight:600;letter-spacing:.3px}
.footer-text{color:var(--footer-text);font-size:6.6px;line-height:9.5px}
.footer-logo{left:93px;top:1095px;width:147px;height:40px;background:#fff;border-radius:2px;display:flex;align-items:center;justify-content:center;font-size:8px;font-weight:600;color:var(--ink)}
.quick a{display:block;color:var(--footer-text);font-size:6.2px;text-decoration:none;line-height:10.5px}
.quick a span{color:var(--orange);margin-right:7px}
</style>
</head>
<body>

<nav class="abs nav">
  <a class="active" style="left:103px">Home</a>
  <a style="left:141px">About Us</a>
  <a style="left:190px">Services</a>
  <a style="left:236px">Pricing</a>
  <a style="left:278px">Contact Us</a>
  <div class="underline"></div>
</nav>

<header class="abs hero" role="img" aria-label="Aerial photograph of a city skyline at sunset"></header>
<div class="abs hero-logo">RM Skyline Imaging</div>
<h1 class="abs hero-title display">RYAN MARLOWE</h1>
<div class="abs hero-sub display">Aerial Photography</div>

<section class="abs about"></section>
<div class="abs about-label">ABOUT</div>
<div class="abs about-title display">Aerial Photography</div>
<svg class="abs" style="left:258px;top:354px" width="20" height="38" viewBox="0 0 20 38"><polygon points="0,0 20,19 0,38" fill="var(--orange-dark)"/></svg>
<p class="abs about-text">Lorem ipsum dolor sit amet, consectetur adipiscing elit, sed do eiusmod tempor incididunt ut labore et dolore magna aliqua. Ut enim ad minim veniam, quis nostrud exercitation ullamco laboris nisi ut aliquip ex ea commodo consequat. Duis aute irure dolor in reprehenderit in voluptate velit esse cillum dolore eu fugiat nulla pariatur. Excepteur sint occaecat cupidatat non proident.</p>

<section class="abs services"></section>
<h2 class="abs section-head display" style="top:434px;font-size:17px">OUR SERVICES</h2>
<div class="abs services-rule"></div>

<svg class="abs" style="left:93px;top:496px" width="27" height="21" viewBox="0 0 27 21"><rect x="1" y="4" width="25" height="16" rx="2" fill="none" stroke="var(--orange)" stroke-width="1.5"/><rect x="4" y="1" width="6" height="3" fill="none" stroke="var(--orange)" stroke-width="1.2"/><circle cx="13.5" cy="12" r="4.5" fill="none" stroke="var(--orange)" stroke-width="1.5"/></svg>
<div class="abs service-name" style="left:126px;top:503px">PHOTOGRAPHY</div>
<p class="abs service-desc" style="left:93px;top:523px">Drone Photography services include editing, titling, and more.</p>

<svg class="abs" style="left:285px;top:496px" width="22" height="20" viewBox="0 0 22 20"><rect x="1" y="6" width="14" height="10" fill="none" stroke="var(--blue)" stroke-width="1.4"/><circle cx="5" cy="3.5" r="2.5" fill="none" stroke="var(--blue)" stroke-width="1.2"/><circle cx="11" cy="3.5" r="2.5" fill="none" stroke="var(--blue)" stroke-width="1.2"/><polygon points="15,9 21,6 21,16 15,13" fill="none" stroke="var(--blue)" stroke-width="1.2"/><line x1="6" y1="16" x2="4" y2="19" stroke="var(--blue)"/><line x1="10" y1="16" x2="12" y2="19" stroke="var(--blue)"/></svg>
<div class="abs service-name" style="left:313px;top:504px">VIDEOGRAPHY</div>
<p class="abs service-desc" style="left:285px;top:523px">Available Drone Videography services include filming, editing, music, titling and more.</p>

<svg class="abs" style="left:460px;top:497px" width="40" height="20" viewBox="0 0 40 20"><polygon points="1,10 20,1 39,10 20,19" fill="none" stroke="var(--blue)" stroke-width="1.4"/><path d="M7,7 L26,16 M13,4 L32,13 M33,7 L14,16 M27,4 L8,13" stroke="var(--blue)" stroke-width=".7" fill="none"/></svg>
<div class="abs service-name display" style="left:506px;top:503px;font-size:8.5px">3D MAPPING</div>
<p class="abs service-desc" style="left:460px;top:523px">3D Mapping services include 2D Maps, and 3D Models.</p>

<section class="abs pricing" role="img" aria-label="Darkened aerial photograph of city towers"></section>
<div class="abs pricing-title display">PRICING</div>

<div class="abs plan" style="left:93px"><div class="plan-price display">200</div><div class="plan-note display">UP TO 20 EDITED HIGH<br>RESOLUTION IMAGES.</div></div>
<div class="abs plan" style="left:279px"><div class="plan-price display">200</div><div class="plan-note display">RAW AERIAL FOOTAGE<br>AVAILABLE FOR YOU TO USE.</div></div>
<div class="abs plan" style="left:472px"><div class="plan-price display">200</div><div class="plan-note display">3D MODEL</div></div>
<svg class="abs" style="left:228px;top:674px" width="7" height="14" viewBox="0 0 7 14"><polyline points="0,0 6,7 0,14" fill="none" stroke="#e8e8e8"/></svg>
<svg class="abs" style="left:414px;top:674px" width="7" height="14" viewBox="0 0 7 14"><polyline points="0,0 6,7 0,14" fill="none" stroke="#e8e8e8"/></svg>
<p class="abs plan-desc" style="left:93px">Available Drone Photography services include editing, titling, and more.</p>
<p class="abs plan-desc" style="left:279px;width:150px">Available Drone Videography services include filming, editing, music, titling and more.</p>
<p class="abs plan-desc" style="left:472px">Available 3D Mapping services include 2D Maps, and 3D Models.</p>

<section class="abs contact" role="img" aria-label="Faint dotted world map background"></section>
<h2 class="abs section-head display" style="top:808px;font-size:16px">CONTACT US</h2>
<p class="abs" style="left:0;top:832px;width:701px;text-align:center;font-size:7.4px;color:var(--grey)">Excepteur sint occaecat cupidatat non proident, sunt in culpa qui officia</p>
<div class="abs field" style="left:130px;top:875px;width:139px;height:27px">Name</div>
<div class="abs field" style="left:273px;top:875px;width:141px;height:27px">Email</div>
<div class="abs field" style="left:417px;top:875px;width:153px;height:27px">Address</div>
<div class="abs field" style="left:130px;top:912px;width:440px;height:65px">Comments</div>
<div class="abs send">SEND</div>

<footer class="abs footer"></footer>
<div class="abs footer-head" style="left:93px;top:1074px">ABOUT US</div>
<div class="abs footer-logo">RM Skyline Imaging</div>
<p class="abs footer-text" style="left:95px;top:1143px;width:175px">Lorem ipsum dolor sit amet, consectetur adipiscing elit, sed do eiusmod tempor incididunt ut labore et dolore magna aliqua. Ut enim ad minim veniam,</p>
<p class="abs" style="left:95px;top:1180px;font-size:6.6px;color:var(--orange)">©2017 Allrights are Reserved</p>

<div class="abs" style="left:351px;top:1070px;width:1px;height:110px;background:#3d3d3d"></div>

<svg class="abs" style="left:372px;top:1071px" width="9" height="13" viewBox="0 0 9 13"><path d="M4.5,12 C1.5,7.5 .8,6 .8,4.3 A3.7,3.7 0 0 1 8.2,4.3 C8.2,6 7.5,7.5 4.5,12Z" fill="none" stroke="#fff" stroke-width="1.1"/><circle cx="4.5" cy="4.3" r="1.3" fill="#fff"/></svg>
<div class="abs footer-head" style="left:384px;top:1074px">GET IN TOUCH</div>
<p class="abs footer-text" style="left:385px;top:1096px;width:125px">Excepteur sint occaecat cupidatat non proident, sunt in culpa qui officia</p>
<p class="abs footer-text" style="left:385px;top:1122px">Email:&nbsp; info@rmskylineimages.com</p>
<p class="abs footer-text" style="left:385px;top:1137px">Contact no: 001.555.0142</p>
<svg class="abs" style="left:381px;top:1155px" width="70" height="16" viewBox="0 0 70 16"><g fill="none" stroke="var(--orange)" stroke-width="1"><circle cx="8" cy="8" r="7"/><circle cx="25" cy="8" r="7"/><circle cx="42" cy="8" r="7"/><circle cx="59" cy="8" r="7"/></g></svg>

<div class="abs footer-head" style="left:552px;top:1075px;font-weight:400">QUICK LINK</div>
<div class="abs quick" style="left:552px;top:1095px">
  <a><span>»</span>Home</a>
  <a><span>»</span>About Us</a>
  <a><span>»</span>Services</a>
  <a><span>»</span>Pricing</a>
  <a><span>»</span>Contact Us</a>
</div>

</body>
</html>
```